Podiatry (services) Business Card

I need a business design for a New Podiatry Service.
the Podiatry services will include all aspects of podiatry including;
general podiatry for all ages
corns and callus treatment
Ingrown toenails & nail surgery
Forefoot, arch and heel pain
Gait analysis
Sports Podiatry and Orthotics
Paediatric Assessments
Diabetes Foot Assessment

I would like the back of the card to have space for next appointment day and time.

I would like a nice design that is simple yet catchy. I don't like cluttered business cards. I like things to be simple yet stand out because of the finer details.

I like the colours blue and white but I'm open to other designs that have different colours.

Kestrel Podiatry (Business name)

Leisel Marrow - Podiatrist
M.Pod.P., B.Hlth. Sci, MQFotA

Address: 58 Tolbrook Rd, Carrowby North Vic, 3198
Phone: (03) 9564 2718
Fax: (03) 9432 6581

```html
<!DOCTYPE html>
<html lang="en">
<head>
<meta charset="utf-8">
<title>Kestrel Podiatry – Business Cards</title>
<link href="https://fonts.googleapis.com/css2?family=Libre+Baskerville:wght@400;700&family=Questrial&display=swap" rel="stylesheet">
<style>
  :root {
    --backdrop: #e8e5e0;
    --card: #ffffff;
    --brand-blue: #3457a7;
    --band-light: #4a6cb8;
    --navy: #2a3f8f;
    --sky: #3f7fd0;
    --white: #ffffff;
    --serif: "Libre Baskerville", Georgia, serif;
    --sans: "Questrial", Arial, sans-serif;
  }
  * { box-sizing: border-box; margin: 0; padding: 0; }
  html, body { width: 1200px; height: 789px; overflow: hidden; }
  body { background: var(--backdrop); position: relative; }

  .card {
    position: absolute;
    top: 234px;
    width: 560px;
    height: 320px;
    background: var(--card);
    box-shadow: 0 8px 24px rgba(0,0,0,0.15);
    overflow: hidden;
  }
  .card--appointment { left: 30px; }
  .card--contact { left: 610px; }

  .card__shapes { position: absolute; inset: 0; }

  .brand {
    position: absolute;
    display: flex;
    align-items: center;
    gap: 10px;
    font-family: var(--serif);
    font-weight: 400;
    color: var(--navy);
    white-space: nowrap;
  }
  .brand__dot {
    border-radius: 50%;
    background: var(--brand-blue);
    flex: none;
  }
  .card--appointment .brand { left: 34px; top: 112px; font-size: 33px; }
  .card--appointment .brand__dot { width: 16px; height: 16px; }
  .card--contact .brand { left: 26px; top: 44px; font-size: 22px; }
  .card--contact .brand__dot { width: 11px; height: 11px; }

  /* appointment strip */
  .appointment {
    position: absolute;
    font-family: var(--sans);
    color: var(--brand-blue);
    font-size: 14px;
    white-space: nowrap;
  }
  .appointment__label { left: 130px; top: 280px; }
  .appointment__field { display: flex; align-items: flex-end; gap: 4px; }
  .appointment__field--date { left: 190px; top: 298px; }
  .appointment__field--time { left: 390px; top: 280px; }
  .appointment__blank {
    display: inline-block;
    border-bottom: 1.5px dotted var(--brand-blue);
    height: 12px;
  }
  .appointment__field--date .appointment__blank { width: 160px; }
  .appointment__field--time .appointment__blank { width: 130px; }

  /* contact card */
  .rule {
    position: absolute;
    left: 316px;
    right: 0;
    top: 57px;
    height: 1.5px;
    background: var(--navy);
  }
  .person {
    position: absolute;
    right: 26px;
    top: 92px;
    text-align: right;
    font-family: var(--serif);
    white-space: nowrap;
  }
  .person__name {
    display: flex;
    align-items: center;
    justify-content: flex-end;
    gap: 8px;
    font-size: 19px;
    font-weight: 700;
    color: var(--navy);
  }
  .person__icon {
    width: 22px; height: 22px;
    border-radius: 50%;
    background: var(--sky);
    border: 2px solid var(--sky);
  }
  .person__role {
    display: flex;
    align-items: center;
    justify-content: flex-end;
    gap: 4px;
    margin-right: 30px;
    font-size: 13px;
    color: var(--navy);
  }
  .person__role::before {
    content: "";
    width: 58px;
    height: 1px;
    background: var(--navy);
  }
  .person__credentials {
    margin-top: 8px;
    font-size: 12.5px;
    font-weight: 700;
    color: var(--sky);
  }

  .contact-line {
    position: absolute;
    display: flex;
    align-items: flex-start;
    gap: 10px;
    font-family: var(--serif);
    color: var(--white);
    font-size: 14.5px;
    line-height: 1.45;
    white-space: nowrap;
  }
  .contact-line svg { flex: none; margin-top: 3px; }
  .contact-line--phone { left: 44px; top: 262px; }
  .contact-line--fax { left: 44px; top: 286px; }
  .contact-line--address {
    left: 390px;
    top: 210px;
    font-size: 13px;
    width: 162px;
    white-space: normal;
  }
</style>
</head>
<body>

  <section class="card card--appointment" aria-label="Appointment card">
    <svg class="card__shapes" width="560" height="320" viewBox="0 0 560 320" aria-hidden="true">
      <path fill="var(--brand-blue)"
            d="M400 0 H560 V275 H45 C120 228 300 206 440 196 C512 190 532 150 526 104 C520 50 470 12 400 0 Z"/>
      <rect x="0" y="274" width="50" height="1.5" fill="var(--brand-blue)"/>
    </svg>

    <div class="brand"><span class="brand__dot"></span>Kestrel Podiatry</div>

    <div class="appointment appointment__label">Next appointment,</div>
    <div class="appointment appointment__field appointment__field--date">Date <span class="appointment__blank"></span></div>
    <div class="appointment appointment__field appointment__field--time">Time <span class="appointment__blank"></span></div>
  </section>

  <section class="card card--contact" aria-label="Contact card">
    <svg class="card__shapes" width="560" height="320" viewBox="0 0 560 320" aria-hidden="true">
      <polygon fill="var(--band-light)" points="0,255 351,255 376,320 0,320"/>
      <polygon fill="var(--brand-blue)" points="342,190 560,190 560,320 392,320"/>
    </svg>

    <div class="brand"><span class="brand__dot"></span>Kestrel Podiatry</div>
    <div class="rule"></div>

    <div class="person">
      <div class="person__name">Leisel Marrow <span class="person__icon"></span></div>
      <div class="person__role">Podiatrist</div>
      <div class="person__credentials">M.Pod.P., B.Hlth. Sci, MQFotA</div>
    </div>

    <div class="contact-line contact-line--phone">
      <svg width="14" height="14" viewBox="0 0 14 14" aria-hidden="true">
        <circle cx="7" cy="7" r="7" fill="var(--white)"/>
        <path d="M4.3 3.6 l1.4 -0.3 l0.8 1.8 l-0.9 0.7 a5 5 0 0 0 2.4 2.4 l0.7 -0.9 l1.8 0.8 l-0.3 1.4 a6.5 6.5 0 0 1 -5.9 -5.9 z" fill="var(--band-light)"/>
      </svg>
      <span>(03) 9564 2718</span>
    </div>
    <div class="contact-line contact-line--fax">
      <svg width="14" height="14" viewBox="0 0 14 14" aria-hidden="true">
        <circle cx="7" cy="7" r="7" fill="var(--white)"/>
        <rect x="3.5" y="6" width="7" height="4" rx="0.6" fill="var(--band-light)"/>
        <rect x="5" y="3.5" width="4" height="2.5" fill="var(--band-light)"/>
      </svg>
      <span>(03) 9432 6581</span>
    </div>
    <div class="contact-line contact-line--address">
      <svg width="11" height="15" viewBox="0 0 11 15" aria-hidden="true">
        <path d="M5.5 0 a5.5 5.5 0 0 1 5.5 5.5 c0 3.8 -5.5 9.5 -5.5 9.5 s-5.5 -5.7 -5.5 -9.5 a5.5 5.5 0 0 1 5.5 -5.5 z" fill="var(--white)"/>
        <circle cx="5.5" cy="5.5" r="2" fill="var(--brand-blue)"/>
      </svg>
      <span>58 Tolbrook Rd, Carrowby North Vic, 3198</span>
    </div>
  </section>

</body>
</html>
```